Milk product packaging

We are ready to begin packaging our product! Exciting! I already have a logo (from Pixel Forge!) and company name (Calbrin Ventures), but now we need an attractive, attention-drawing and pleasing package design. The product is a healthy flavored milk that needs to appeal to kids from 2 years old and up, moms shopping for kids, and potentially other adults. A hard task, but we don't want to limit the product to kids even though they will be the first customer we will advertise to.

The product will most likely be a flexa bok single serving milk package, like the kind kids take in their lunch boxes, that has a straw attached. It will need to have space for nutritional labeling and space on the back for advertising or things like 'fun facts.'

So far our main logo colors are green, black and white (see the logos attached.) Looking at competitors (Kestrel Organics, Zuba Milk, Bramlow Fields) they have used components of farms or cows on their products to appeal to a down-to-earth feel and to promote the idea of a product 'straight from the farm.' This isn't a necessity for me but it was something I noted. There will be multiple flavors of milk, and so far I've been using a bluish purple color for the Radiance blend (which contains blue and purple berries) and a dark yellow for the Calmora blend, an accent to the standard black/white/green color scheme of the logo and materials. So all packages look the same, but a different flavor has a different 'splash' of color to differentiate it. Again, just my thoughts and i'm open to other looks and ideas. We're advertising it as "milk plus a nourishing blend of ....." Statistics say we only have 3-5 seconds to influence the customer to pick up and try our product, so we're looking for a winning design to help us do just that!! We want to lead the way in flavored milk that is healthy, not just added sugar and artificial ingredients. The attached files are the logos we got from Pixel Forge. Healthy, nourishing, flavored milk!

Reason: Hi! Many designers seem to be busy...just seeing if this helps. So far I love the ideas I'm seeing! Thanks.

```html
<!DOCTYPE html>
<html lang="en">
<head>
<meta charset="utf-8">
<title>Calbrin Ventures – Calmora blend carton</title>
<link rel="stylesheet" href="https://fonts.googleapis.com/css2?family=Fredoka:wght@600&family=Sriracha&family=Montserrat:wght@800&display=swap">
<style>
  :root {
    --leaf-green: #8cc63f;
    --leaf-green-deep: #62a83a;
    --band-orange: #f7941d;
    --band-red: #ef4e23;
    --milk-white: #ffffff;
    --milk-shade: #e2e2e2;
    --flavour-orange: #f08a24;
    --tagline-green: #a6d13c;
    --meadow-light: #a8d54c;
    --meadow-deep: #4e9a3a;
  }
  * { margin: 0; padding: 0; box-sizing: border-box; }
  html, body { width: 1200px; height: 3465px; overflow: hidden; }
  body { background: #ffffff; }

  .carton {
    position: relative;
    width: 1200px;
    height: 3465px;
    overflow: hidden;
    background: linear-gradient(180deg, var(--leaf-green) 0%, var(--leaf-green-deep) 100%);
  }

  .flavour-band {
    position: absolute;
    left: 202px;
    width: 795px;
    top: 0;
    height: 3465px;
    background: linear-gradient(180deg, var(--band-orange) 0%, var(--band-orange) 12%, var(--band-red) 45%, var(--band-red) 100%);
  }

  .brand {
    position: absolute;
    left: 0;
    width: 1200px;
    top: 300px;
    text-align: center;
  }
  .brand-mark {
    width: 420px;
    height: 420px;
    margin: 0 auto 50px;
    border-radius: 50%;
    background: var(--milk-white);
  }
  .brand-name {
    font-family: "Fredoka", sans-serif;
    font-weight: 600;
    color: var(--milk-white);
    line-height: 1;
  }
  .brand-name .line-one { display: block; font-size: 205px; }
  .brand-name .line-two { display: block; font-size: 160px; margin-top: 0; }

  .milk-splash {
    position: absolute;
    left: 0;
    top: 1220px;
    width: 1200px;
    height: 1420px;
    background: radial-gradient(ellipse at 50% 50%, var(--milk-white) 0%, #f6f6f6 55%, var(--milk-shade) 100%);
  }

  .flavour-name {
    position: absolute;
    left: 0;
    width: 1240px;
    top: 1740px;
    text-align: center;
    font-family: "Sriracha", cursive;
    color: var(--flavour-orange);
    line-height: 1.05;
  }
  .flavour-name .name { display: block; font-size: 150px; }
  .flavour-name .kind { display: block; font-size: 130px; }

  .meadow {
    position: absolute;
    top: 2730px;
    height: 735px;
    background: linear-gradient(180deg, var(--meadow-deep) 0%, var(--meadow-light) 100%);
  }
  .meadow-left { left: 0; width: 202px; }
  .meadow-right { left: 997px; width: 203px; }

  .tagline {
    position: absolute;
    left: 202px;
    width: 795px;
    top: 2715px;
    text-align: center;
    font-family: "Sriracha", cursive;
    color: var(--tagline-green);
    line-height: 1.12;
  }
  .tagline .lead { display: block; font-size: 100px; }
  .tagline .middle { display: block; font-size: 74px; }

  .volume {
    position: absolute;
    left: 0;
    width: 1200px;
    top: 3300px;
    text-align: center;
    font-family: "Montserrat", sans-serif;
    font-weight: 800;
    font-size: 62px;
    color: var(--milk-white);
    letter-spacing: 1px;
  }
</style>
</head>
<body>
<main class="carton">
  <div class="flavour-band"></div>

  <header class="brand">
    <div class="brand-mark"></div>
    <h1 class="brand-name">
      <span class="line-one">Calbrin</span>
      <span class="line-two">Ventures</span>
    </h1>
  </header>

  <div class="milk-splash" role="img" aria-label="Illustration of a white milk splash crown across the carton"></div>

  <div class="flavour-name">
    <span class="name">Calmora</span>
    <span class="kind">blend</span>
  </div>

  <div class="meadow meadow-left" role="img" aria-label="Illustration of green hills and trees with a white cow silhouette"></div>
  <div class="meadow meadow-right" role="img" aria-label="Illustration of green hills and trees"></div>

  <p class="tagline">
    <span class="lead">Healthy milk</span>
    <span class="middle">with the goodness</span>
    <span class="lead">of Ginger</span>
  </p>

  <p class="volume">3 FL OZ (236 ml)</p>
</main>
</body>
</html>
```